Updated DJ business Card showing other businesses

DJ Kestro offers professional mobile dj services including DJ. MC. Karaoke.
Hushbeat (will attach logo)
I also offer a 360 Photo Booth.

Contact info:
(555) 013-4472
marcus.tellgren@lumomail.net
Social Media @DJKestroNWX

```html
<!DOCTYPE html>
<html lang="en">
<head>
<meta charset="UTF-8">
<title>DJ Kestro Business Card</title>
<link href="https://fonts.googleapis.com/css2?family=Poppins:wght@400;500;700;800&display=swap" rel="stylesheet">
<style>
  :root {
    --stage: #2d2d2d;
    --paper: #ffffff;
    --brand-red: #d7204b;
    --ink: #0a0a0a;
  }
  html, body {
    margin: 0;
    padding: 0;
    width: 1200px;
    height: 1200px;
    overflow: hidden;
    background: var(--stage);
    font-family: "Poppins", Arial, sans-serif;
  }
  .card {
    position: absolute;
    left: 175px;
    width: 850px;
    height: 510px;
    box-shadow: 0 6px 18px rgba(0,0,0,0.45);
    overflow: hidden;
  }
  .card-front { top: 65px; background: var(--paper); }
  .card-back { top: 632px; background: var(--brand-red); }

  .brand-name {
    position: absolute;
    left: 58px;
    top: 72px;
    margin: 0;
    font-weight: 800;
    font-size: 64px;
    letter-spacing: -1px;
    line-height: 1;
    color: var(--ink);
  }
  .partner {
    position: absolute;
    left: 515px;
    top: 78px;
    display: flex;
    align-items: center;
    gap: 14px;
  }
  .partner-dot {
    width: 60px;
    height: 60px;
    border-radius: 50%;
    border: 3px solid var(--ink);
    box-sizing: border-box;
  }
  .partner-name {
    font-weight: 800;
    font-size: 44px;
    line-height: 1;
    color: var(--ink);
  }
  .tagline {
    position: absolute;
    left: 0;
    right: 0;
    top: 190px;
    margin: 0;
    text-align: center;
    font-weight: 700;
    font-size: 30px;
    color: var(--brand-red);
  }
  .services {
    position: absolute;
    left: 0;
    right: 0;
    top: 234px;
    margin: 0;
    text-align: center;
    font-weight: 400;
    font-size: 28px;
    color: var(--ink);
    word-spacing: 4px;
  }
  .services .sep { margin: 0 14px; }
  .contact-list {
    position: absolute;
    left: 261px;
    top: 308px;
    margin: 0;
    padding: 0;
    list-style: none;
  }
  .contact-item {
    display: flex;
    align-items: center;
    height: 38px;
    font-size: 21px;
    font-weight: 500;
    color: var(--ink);
  }
  .contact-icon {
    width: 28px;
    height: 28px;
    margin-right: 12px;
    flex: none;
  }
  .social-dot {
    width: 24px;
    height: 24px;
    border: 2px solid var(--brand-red);
    border-radius: 50%;
    margin-right: 14px;
    flex: none;
  }
  .bands {
    position: absolute;
    left: 0;
    top: 435px;
    width: 850px;
    height: 17px;
  }
  .back-name {
    position: absolute;
    left: 0;
    right: 0;
    top: 190px;
    margin: 0;
    text-align: center;
    font-weight: 800;
    font-size: 112px;
    line-height: 1;
    letter-spacing: -2px;
    color: var(--paper);
  }
</style>
</head>
<body>
  <section class="card card-front">
    <h1 class="brand-name">DJ Kestro</h1>
    <div class="partner">
      <span class="partner-dot"></span>
      <span class="partner-name">Hushbeat</span>
    </div>
    <p class="tagline">Professional Mobile DJ Service</p>
    <p class="services">DJ<span class="sep">•</span>MC<span class="sep">•</span>Karaoke<span class="sep">•</span>360 Photo Booth</p>
    <ul class="contact-list">
      <li class="contact-item">
        <svg class="contact-icon" viewBox="0 0 28 28" aria-hidden="true">
          <circle cx="14" cy="14" r="12.5" fill="none" stroke="#d7204b" stroke-width="1.6"/>
          <path d="M9 8.5c1-1 2-.8 2.5 0l1.3 2.2c.4.7.2 1.4-.4 1.8l-.8.5c.6 1.6 1.8 2.8 3.4 3.4l.5-.8c.4-.6 1.1-.8 1.8-.4l2.2 1.3c.8.5 1 1.5 0 2.5-1 1-2.6 1.2-4.6.2-2.7-1.3-4.7-3.3-6-6-1-2-.8-3.6.1-4.7z" fill="none" stroke="#d7204b" stroke-width="1.4"/>
        </svg>
        (555) 013-4472
      </li>
      <li class="contact-item">
        <svg class="contact-icon" viewBox="0 0 28 28" aria-hidden="true">
          <circle cx="14" cy="14" r="12.5" fill="none" stroke="#d7204b" stroke-width="1.6"/>
          <rect x="7.5" y="9.5" width="13" height="9" fill="none" stroke="#d7204b" stroke-width="1.4"/>
          <path d="M7.5 9.5l6.5 5 6.5-5M7.5 18.5l4.8-4.2M20.5 18.5l-4.8-4.2" fill="none" stroke="#d7204b" stroke-width="1.4"/>
        </svg>
        marcus.tellgren@lumomail.net
      </li>
      <li class="contact-item">
        <span class="social-dot"></span>
        <span class="social-dot"></span>
        @DJKestroNWX
      </li>
    </ul>
    <svg class="bands" viewBox="0 0 850 17" aria-hidden="true">
      <polygon points="0,0 266,0 252,17 0,17" fill="#d7204b"/>
      <polygon points="283,0 850,0 850,17 269,17" fill="#0a0a0a"/>
    </svg>
  </section>

  <section class="card card-back">
    <p class="back-name">DJ Kestro</p>
  </section>
</body>
</html>
```